Small CPA firm
Project: Business cards and stationary
Business cards and stationary - Financial Services
Business cards and stationary
Professional
Darren P. Holcomb
Certified Public Accountant
418 Birchmont Lane, 4-120 Mobile, Alabama 36609
dh@dholcombcpa.example
www.dholcombcpa.example
I'd like a professional but creative looking business card and stationary using my logo. For the business card, I think I would like a design with the logo on the top or the left side, with my name and contact information on the bottom (for logo on top) or right hand side (for logo on left). I'd like to use the same primary colors that the logo uses.
For the back of the card, I think I'd like just the logo without the words in an appropriate format.

```html
<!DOCTYPE html>
<html lang="en">
<head>
<meta charset="utf-8">
<title>Darren P. Holcomb CPA – Business Card</title>
<link rel="stylesheet" href="https://fonts.googleapis.com/css2?family=Cinzel:wght@400;600;700&family=Tinos&display=swap">
<style>
  :root {
    --page-bg: #e9e7e3;
    --card-white: #ffffff;
    --card-shade: #e6e8ec;
    --sky: #35aee0;
    --ocean: #1f5d9e;
    --navy: #1b2f6e;
    --ink: #1a1a1a;
    --icon: #2a3f7a;
  }
  * { margin: 0; padding: 0; box-sizing: border-box; }
  html, body { width: 1200px; height: 804px; overflow: hidden; background: var(--page-bg); }
  .canvas { position: relative; width: 1200px; height: 804px; }
  .card {
    position: absolute; left: 110px; top: 132px; width: 980px; height: 540px;
    border-radius: 34px; overflow: hidden;
    background: linear-gradient(180deg, var(--card-white) 60%, var(--card-shade) 100%);
    box-shadow: 0 8px 22px rgba(0,0,0,.22);
  }
  .card-swoosh { position: absolute; inset: 0; }
  .holder { position: absolute; right: 36px; top: 22px; text-align: right; color: #fff; font-family: "Cinzel", serif; }
  .holder-name { font-size: 31px; font-weight: 600; line-height: 1.1; }
  .holder-title { font-size: 19px; font-weight: 700; margin-top: 4px; }
  .firm { position: absolute; left: 56px; top: 150px; display: flex; align-items: center; }
  .firm-mark { width: 108px; height: 108px; border-radius: 50%; background: var(--ocean); flex: none; }
  .firm-text { margin-left: 20px; color: var(--navy); font-family: "Cinzel", serif; }
  .firm-name { font-size: 35px; font-weight: 600; line-height: 1; white-space: nowrap; }
  .firm-tagline { font-size: 18px; font-weight: 600; margin-top: 8px; white-space: nowrap; }
  .contact { position: absolute; left: 53px; top: 292px; font-family: "Tinos", serif; color: var(--ink); }
  .address { font-size: 26px; margin-bottom: 14px; }
  .contact-list { list-style: none; }
  .contact-list li { display: flex; align-items: center; font-size: 24px; height: 34px; }
  .contact-list svg { width: 20px; height: 20px; margin-right: 18px; margin-left: 6px; fill: var(--icon); }
</style>
</head>
<body>
<div class="canvas">
  <section class="card">
    <svg class="card-swoosh" viewBox="0 0 980 540" width="980" height="540" aria-hidden="true">
      <defs>
        <linearGradient id="bandGradient" x1="0" y1="0" x2="1" y2="0.3">
          <stop offset="0" stop-color="var(--sky)"/>
          <stop offset="1" stop-color="var(--ocean)"/>
        </linearGradient>
      </defs>
      <path d="M0,0 H980 V470 C945,290 855,172 700,140 C520,108 250,118 0,128 Z" fill="var(--navy)"/>
      <path d="M0,0 H980 V400 C950,260 860,142 700,112 C520,80 250,90 0,100 Z" fill="url(#bandGradient)"/>
    </svg>

    <div class="holder">
      <p class="holder-name">Darren P. Holcomb</p>
      <p class="holder-title">Certified Public Accountant</p>
    </div>

    <div class="firm">
      <div class="firm-mark"></div>
      <div class="firm-text">
        <p class="firm-name">Darren P. Holcomb Cpa Llc</p>
        <p class="firm-tagline">Certified Public Accountant and Advisor</p>
      </div>
    </div>

    <div class="contact">
      <p class="address">418 Birchmont Lane, 4-120, Mobile, Alabama 36609</p>
      <ul class="contact-list">
        <li><svg viewBox="0 0 20 20"><path d="M4 2 L8 2 L9 6 L7 8 C8 11 10 13 12 14 L14 12 L18 13 L18 17 C18 18 17 19 16 19 C8 18 2 12 1 4 C1 3 2 2 4 2 Z"/></svg>(251) 555-0181</li>
        <li><svg viewBox="0 0 20 20"><path d="M6 1 H14 A1.5 1.5 0 0 1 15.5 2.5 V17.5 A1.5 1.5 0 0 1 14 19 H6 A1.5 1.5 0 0 1 4.5 17.5 V2.5 A1.5 1.5 0 0 1 6 1 Z M6.5 3.5 V14.5 H13.5 V3.5 Z"/></svg>(251) 555-0147</li>
        <li><svg viewBox="0 0 20 20"><path d="M5 1 H13 V6 H5 Z M2 7 H18 V15 H15 V19 H5 V15 H2 Z M7 13 V17 H13 V13 Z"/></svg>(251) 555-0193</li>
        <li><svg viewBox="0 0 20 20"><path d="M1 4 H19 V16 H1 Z M3 6 L10 11 L17 6 V5.5 H3 Z"/></svg>dh@dholcombcpa.example</li>
        <li><svg viewBox="0 0 20 20"><path d="M10 1 A9 9 0 1 0 10.01 1 Z M10 3 A7 7 0 0 1 16.9 9 H13.4 C13.3 6.6 12.6 4.5 11.5 3.2 Z M8.5 3.2 C7.4 4.5 6.7 6.6 6.6 9 H3.1 A7 7 0 0 1 8.5 3.2 Z M8.6 9 C8.7 6.8 9.3 5 10 4 C10.7 5 11.3 6.8 11.4 9 Z M3.1 11 H6.6 C6.7 13.4 7.4 15.5 8.5 16.8 A7 7 0 0 1 3.1 11 Z M8.6 11 H11.4 C11.3 13.2 10.7 15 10 16 C9.3 15 8.7 13.2 8.6 11 Z M13.4 11 H16.9 A7 7 0 0 1 11.5 16.8 C12.6 15.5 13.3 13.4 13.4 11 Z"/></svg>www.dholcombcpa.example</li>
      </ul>
    </div>
  </section>
</div>
</body>
</html>
```